Website Design for The Lamp Corner (Online Furniture Retailer)

Complete redesign of furniture commerce website using the latest trends. Blank canvas to work with!

```html
<!DOCTYPE html>
<html lang="en">
<head>
<meta charset="utf-8">
<title>The Lamp Corner</title>
<link href="https://fonts.googleapis.com/css2?family=Arimo:wght@400;700&family=Crimson+Text&family=PT+Sans:wght@400;700&family=Ubuntu:wght@400;500&display=swap" rel="stylesheet">
<style>
:root{
  --blue:#1ba3d9;
  --blue-light:#4cc2ec;
  --blue-dark:#0f86bb;
  --link:#1a6fa3;
  --green:#8cc21f;
  --green-light:#b6dc4a;
  --green-dark:#6ea30e;
  --text:#333;
  --muted:#666;
  --line:#dcdcdc;
  --panel:#f3f3f3;
  --white:#fff;
}
*{margin:0;padding:0;box-sizing:border-box}
html,body{width:1200px;height:2313px;overflow:hidden;background:var(--white)}
body{position:relative;font-family:"Arimo",Arial,sans-serif;color:var(--text)}
.abs{position:absolute}
ul{list-style:none}

/* header */
.brand{left:188px;top:14px;display:flex;align-items:center;gap:12px}
.brand-mark{width:46px;height:46px;background:var(--blue)}
.brand-name{font-family:"Crimson Text",serif;font-size:38px;color:var(--blue);line-height:1}
.hotline{right:189px;top:14px;text-align:right;font-family:"Ubuntu",sans-serif;color:var(--blue);line-height:1.05}
.hotline .call{font-size:22px}
.hotline .hours{font-size:17px}

.navbar{left:0;top:76px;width:1200px;height:37px;background:linear-gradient(#fafafa,#ececec);border-top:1px solid var(--line);border-bottom:1px solid var(--line)}
.nav{position:absolute;left:187px;top:0;display:flex;height:35px}
.nav li{font-size:12px;color:var(--blue);padding:0 11px;line-height:35px;border-right:1px solid var(--line)}
.nav li.active{background:var(--blue);color:#fff;padding:0 16px}
.cart{position:absolute;right:190px;top:8px;display:flex;align-items:center;gap:10px;font-size:11px;color:var(--blue)}

/* banner */
.hero{left:184px;top:141px;width:827px;height:322px;border:1px solid var(--line);background:#fff;box-shadow:0 14px 18px -14px rgba(0,0,0,.25)}
.hero-photo{position:absolute;left:10px;top:10px;width:805px;height:302px;background:linear-gradient(90deg,#f4f4f4,#e6e6e6 55%,#d9d9d9)}
.hero-curve{position:absolute;left:10px;top:10px}
.hero-copy{position:absolute;left:30px;top:34px;width:262px;color:#fff}
.hero-copy h1{font-family:"PT Sans",sans-serif;font-weight:400;font-size:26px;letter-spacing:.3px;white-space:nowrap}
.hero-copy p{font-size:10.5px;line-height:14.5px;margin-top:12px}
.buy{position:absolute;left:60px;top:213px;width:123px;height:34px;background:linear-gradient(var(--green-light),var(--green-dark));color:#fff;font-size:14px;text-align:center;line-height:34px;border:1px solid #fff}

/* sidebar */
.box{left:188px;width:197px;border:1px solid var(--line);background:#fff;box-shadow:0 1px 2px rgba(0,0,0,.08)}
.box h2{height:34px;background:linear-gradient(var(--blue-light),var(--blue));color:#fff;font-family:"PT Sans",sans-serif;font-weight:400;font-size:19px;line-height:34px;padding-left:9px}
.search{margin:10px 5px;height:26px;border:1px solid var(--line);font-size:12px;color:#555;line-height:24px;padding-left:10px;position:relative}
.search svg{position:absolute;right:6px;top:4px}
.cats li{height:24px;line-height:24px;font-size:10.5px;color:#444;padding-left:11px;border-bottom:1px solid #e8e8e8;margin:0 4px}
.box p{font-size:10.5px;line-height:12.5px;padding:10px 10px 0;color:#222}
.arrows{padding:12px 9px 8px}
.arrows li{font-size:10.5px;line-height:20.5px;padding-left:16px;position:relative;color:#222}
.arrows li::before{content:"";position:absolute;left:0;top:6px;border-left:6px solid var(--link);border-top:4px solid transparent;border-bottom:4px solid transparent}

/* main */
.bar{left:411px;width:601px;height:37px;background:linear-gradient(var(--green-light),var(--green));color:#fff;font-family:"PT Sans",sans-serif;font-weight:700;font-size:20px;line-height:37px;padding-left:13px;letter-spacing:.5px;border-radius:2px}
.about{left:413px;top:565px;width:597px;font-size:10.5px;line-height:12.4px;color:#222}
.about p{margin-bottom:12px}
.about em{font-style:normal;color:var(--link)}
.product{width:154px}
.product .shot{width:154px;height:129px;border:1px solid var(--line);padding:4px;background:#fff;box-shadow:0 2px 3px rgba(0,0,0,.12)}
.product .shot div{width:100%;height:100%}
.product .tag{margin:8px auto 0;width:146px;height:25px;background:linear-gradient(var(--green-light),var(--green));border:1px solid var(--green-dark);font-size:13px;text-align:center;line-height:23px;color:#1d2b05;border-radius:2px}

/* collection */
.band{left:0;top:1667px;width:1200px;height:370px;background:#eeeeee}
.band-line{left:0;top:1689px;width:1200px;height:3px;background:var(--blue-light)}
.band-tab{left:191px;top:1664px;width:822px;height:53px;background:linear-gradient(var(--blue-light),var(--blue));color:#fff;font-family:"PT Sans",sans-serif;font-weight:400;font-size:16px;line-height:53px;padding-left:14px;box-shadow:0 2px 3px rgba(0,0,0,.2)}
.story{left:191px;width:325px;height:101px;border-bottom:1px dotted #999;display:flex;gap:12px}
.story .thumb{width:64px;height:64px;border:3px solid #fff;box-shadow:0 1px 3px rgba(0,0,0,.25);flex:none}
.story h3{font-weight:400;font-size:14.5px;color:var(--link);margin-top:4px}
.story p{font-size:10.5px;line-height:12.5px;margin-top:5px;color:#222}
.samples-title{left:621px;top:1740px;font-size:14.5px;font-weight:400;color:var(--link)}
.round{width:24px;height:24px;border-radius:50%;background:#fff;border:1px solid #bbb;box-shadow:0 1px 2px rgba(0,0,0,.2)}
.swatch{top:1787px;width:64px;height:66px;border:3px solid #fff;box-shadow:0 1px 3px rgba(0,0,0,.25)}
.samples-text{left:621px;top:1880px;width:392px;font-size:12.5px;line-height:13.5px;color:#333}
.view-all{left:627px;top:1963px;width:128px;height:26px;background:linear-gradient(var(--blue-light),var(--blue-dark));color:#fff;font-size:10.5px;line-height:26px;padding-left:9px;border:1px solid #0b6d99}

/* footer */
.foot{left:0;top:2037px;width:1200px;height:227px;background:#f4f4f4;border-top:3px solid var(--blue-light)}
.fcol{top:2066px}
.fcol h4{font-family:"PT Sans",sans-serif;font-weight:400;font-size:18px;color:#222;margin-bottom:10px}
.fcol li{font-size:12px;line-height:25.5px;color:#333;padding-left:19px;position:relative}
.fcol li::before{content:"";position:absolute;left:0;top:7px;width:10px;height:10px;border-radius:50%;border:1px solid #bbb;background:#fff}
.fcol li::after{content:"";position:absolute;left:4px;top:10px;border-left:3px solid #777;border-top:2.5px solid transparent;border-bottom:2.5px solid transparent}
.base{left:0;top:2264px;width:1200px;height:49px;background:linear-gradient(var(--blue-light),var(--blue))}
.legal{position:absolute;left:188px;top:11px;font-size:10px;line-height:12px;color:#e8f7ff}
.partner-badge{position:absolute;left:853px;top:9px;width:158px;height:34px;background:#e6e6e6;border:1px solid #c8c8c8}
</style>
</head>
<body>

<header>
  <div class="abs brand"><span class="brand-mark"></span><span class="brand-name">The Lamp Corner</span></div>
  <div class="abs hotline"><div class="call">Call Free: 0800 555 0192</div><div class="hours">Open 9am - 7pm Everyday</div></div>
  <nav class="abs navbar">
    <ul class="nav">
      <li class="active">Home</li><li>Products</li><li>About us</li><li>Delivery</li><li>Contact Us</li><li>My Account</li>
    </ul>
    <div class="cart">
      <svg width="26" height="20" viewBox="0 0 26 20"><path d="M1 2h4l3 11h13l3-8H7" fill="none" stroke="#777" stroke-width="1.6"/><circle cx="10" cy="17" r="1.8" fill="#777"/><circle cx="19" cy="17" r="1.8" fill="#777"/></svg>
      <span>View Cart | 0 items</span>
    </div>
  </nav>
</header>

<section class="abs hero">
  <div class="hero-photo" role="img" aria-label="Photo of a modern low black upholstered bed with cream bedding between two bedside tables with lamps"></div>
  <svg class="hero-curve" width="470" height="302" viewBox="0 0 470 302">
    <defs><linearGradient id="heroBlue" x1="0" y1="0" x2="1" y2="1"><stop offset="0" stop-color="#2fb3e6"/><stop offset="1" stop-color="#0f93cc"/></linearGradient></defs>
    <path d="M0 0H460C330 40 250 140 270 302H0Z" fill="#bfe8f8"/>
    <path d="M0 0H440C310 40 230 140 250 302H0Z" fill="url(#heroBlue)"/>
  </svg>
  <div class="hero-copy">
    <h1>LOREM IPSUM IS SIMPLY</h1>
    <p>Lorem Ipsum is simply dummy text of the printing and typesetting industry. Lorem Ipsum has been the industry's standard dummy<br>text ever since the 1500s, when an unknown printer took a galley of type and scrambled it to make a</p>
  </div>
  <div class="buy">Buy Now</div>
</section>

<aside>
  <div class="abs box" style="top:513px;height:88px">
    <h2>Search</h2>
    <div class="search">Search Products
      <svg width="16" height="16" viewBox="0 0 16 16"><circle cx="10" cy="6" r="4.5" fill="none" stroke="#333" stroke-width="1.6"/><path d="M7 9L2 14" stroke="#333" stroke-width="2.2"/></svg>
    </div>
  </div>
  <div class="abs box" style="top:635px;height:382px">
    <h2>Category</h2>
    <ul class="cats" style="margin-top:4px">
      <li>Adjustable Beds</li><li>Bean Bags</li><li>Bedroom Furnitures</li><li>Bunk Beds</li><li>Cabin Beds</li><li>Day Beds</li><li>Divan Sets</li><li>Fox Leather Beds</li><li>Adjustable Beds</li><li>Bean Bags</li><li>Bedroom Furnitures</li><li>Bunk Beds</li><li>Cabin Beds</li><li>Day Beds</li>
    </ul>
  </div>
  <div class="abs box" style="top:1049px;height:242px">
    <h2>Bed Guides</h2>
    <p>Whether your troubled by jargon or just generally curious about beds, our guides prove a great read.</p>
    <ul class="arrows"><li>Product Guide</li><li>Memory Foam</li><li>Spring Systems</li><li>Sleep Tips</li><li>PDF Catalogue</li><li>Product Range</li></ul>
  </div>
  <div class="abs box" style="top:1323px;height:278px">
    <h2>Customer Service</h2>
    <p>At The Lamp Corner we like to really look after our customers, why not read through the helpful information below?</p>
    <ul class="arrows"><li>Overview</li><li>Store &amp; Showroom</li><li>Testimonials</li><li>Delivery &amp; Returns</li><li>Contact Us</li><li>Privacy Notice</li><li>Terms &amp; Conditions</li><li>Site Map</li></ul>
  </div>
</aside>

<main>
  <h2 class="abs bar" style="top:513px">About The Lamp Corner</h2>
  <div class="abs about">
    <p>At The Lamp Corner we aim to provide the <em>most extensive selection of beds, mattresses, bedroom furniture and accessories</em> in the UK. To ensure that shopping online with us is an enjoyable experience, our comprehensive <em>online product range</em> is supported by our experienced <em>customer service team</em>, based at our head office in Leeds.</p>
    <p>We have combined the <em>latest technology</em>, with our <em>expert specialist product knowledge</em>, resulting in an online furniture facility which is <em>unrivalled by our competitors</em>.</p>
    <p>With our <em>ever expanding selection of beds and mattresses</em> you'll be sure to find exactly what your looking for. Our fantastic range includes adjustable beds, bedroom furniture, bunk beds, contract beds, divan sets, faux leather beds, guest beds, headboards, leather beds, mattresses, metal beds, novelty beds, oak beds, pine beds, suede beds, wooden beds and much more.</p>
    <p>Combine all this with the <em>best prices on the internet</em> and our <em>award winning delivery service</em>, and we hope you'll see the benefit in shopping with <em>The Lamp Corner</em>.</p>
  </div>

  <h2 class="abs bar" style="top:796px">Featured Products</h2>

  <div class="abs product" style="left:413px;top:851px"><div class="shot"><div role="img" aria-label="Photo of a dark leather bed with white bedding" style="background:linear-gradient(#4a4a4a,#d8d8d8 55%,#2e2e2e)"></div></div><div class="tag">Adjustable Beds</div></div>
  <div class="abs product" style="left:637px;top:851px"><div class="shot"><div role="img" aria-label="Photo of a round bed in a grey modern room" style="background:linear-gradient(#9a9a9a,#cfcfcf 50%,#3a3a3a)"></div></div><div class="tag">Bean Bags</div></div>
  <div class="abs product" style="left:857px;top:851px"><div class="shot"><div role="img" aria-label="Photo of a bed with cream patterned covers and dark headboard" style="background:linear-gradient(#5a4030,#e9e2d4 55%,#3a2a20)"></div></div><div class="tag">Bedroom Furnitures</div></div>

  <div class="abs product" style="left:413px;top:1047px"><div class="shot"><div role="img" aria-label="Photo of a dark wooden four-post bed" style="background:linear-gradient(#c9b89a,#3b2a1c 55%,#8c7456)"></div></div><div class="tag">Adjustable Beds</div></div>
  <div class="abs product" style="left:637px;top:1047px"><div class="shot"><div role="img" aria-label="Photo of a low bed with teal covers by large windows" style="background:linear-gradient(#d8d0c4,#2f5560 55%,#1e1e1e)"></div></div><div class="tag">Bean Bags</div></div>
  <div class="abs product" style="left:857px;top:1047px"><div class="shot"><div role="img" aria-label="Photo of a pink and purple child's bedroom" style="background:linear-gradient(#f2d6e4,#d98fc0 55%,#f5e6ee)"></div></div><div class="tag">Bedroom Furnitures</div></div>

  <div class="abs product" style="left:413px;top:1235px"><div class="shot"><div role="img" aria-label="Photo of a bed with coral pink bedding and cushions" style="background:linear-gradient(#7a4a38,#e47a68 50%,#c8604f)"></div></div><div class="tag">Adjustable Beds</div></div>
  <div class="abs product" style="left:637px;top:1235px"><div class="shot"><div role="img" aria-label="Photo of a minimal bedroom with beige bed" style="background:linear-gradient(#e8e6e2,#c7c1b6 55%,#8f877a)"></div></div><div class="tag">Bean Bags</div></div>
  <div class="abs product" style="left:857px;top:1235px"><div class="shot"><div role="img" aria-label="Photo of a red modern bed in a bright room" style="background:linear-gradient(#5c5c5c,#e8e8e8 45%,#d4342b)"></div></div><div class="tag">Bedroom Furnitures</div></div>

  <div class="abs product" style="left:413px;top:1429px"><div class="shot"><div role="img" aria-label="Photo of a bed with brown patterned throw" style="background:linear-gradient(#d9d4cc,#b9b1a5 45%,#7a4b22)"></div></div><div class="tag">Adjustable Beds</div></div>
  <div class="abs product" style="left:637px;top:1429px"><div class="shot"><div role="img" aria-label="Photo of a brown leather bed in a warm room" style="background:linear-gradient(#c8b397,#5b3d27 55%,#d8c8b0)"></div></div><div class="tag">Bean Bags</div></div>
  <div class="abs product" style="left:857px;top:1429px"><div class="shot"><div role="img" aria-label="Photo of a white bed with black shelving" style="background:linear-gradient(#f2f2f2,#d9d9d9 50%,#2a2a2a)"></div></div><div class="tag">Bedroom Furnitures</div></div>
</main>

<section>
  <div class="abs band"></div>
  <div class="abs band-line"></div>
  <h2 class="abs band-tab">The Kensal Bedroom Furniture Collection</h2>

  <article class="abs story" style="top:1744px">
    <div class="thumb" role="img" aria-label="Photo of a dark bedroom set" style="background:linear-gradient(#3c4a52,#9aa5aa)"></div>
    <div><h3>Lorest Nesto Furmer Et Alust</h3><p>One in about every 10 adults you see walking<br>around doesn't have a job right now.</p></div>
  </article>
  <article class="abs story" style="top:1845px">
    <div class="thumb" role="img" aria-label="Photo of a bed with dark headboard" style="background:linear-gradient(#d8d0c4,#3a2e26)"></div>
    <div><h3>Cras At Adiscipin Dicum</h3><p>150-in 1080p high definition immersive TV<br>for under $1,000? Yeah right. What about<br>a......</p></div>
  </article>
  <article class="abs story" style="top:1949px;border-bottom:0">
    <div class="thumb" role="img" aria-label="Photo of a pink and black chest of drawers" style="background:linear-gradient(#e0407a,#2a2a2a)"></div>
    <div><h3>Quam Massa</h3><p>It seems like every year it gets harder and<br>harder to find the perfect gift for dad.</p></div>
  </article>

  <h3 class="abs samples-title">Some Sample Colour Combinations</h3>
  <div class="abs round" style="left:633px;top:1809px"><svg width="22" height="22" viewBox="0 0 22 22"><path d="M13 6l-5 5 5 5" fill="none" stroke="#222" stroke-width="2.4"/></svg></div>
  <div class="abs round" style="left:982px;top:1809px"><svg width="22" height="22" viewBox="0 0 22 22"><path d="M9 6l5 5-5 5" fill="none" stroke="#222" stroke-width="2.4"/></svg></div>
  <div class="abs swatch" style="left:670px;background:linear-gradient(#f0f0f0,#e8c43a)" role="img" aria-label="Photo of a yellow furniture colour option"></div>
  <div class="abs swatch" style="left:782px;background:linear-gradient(#e8a6c6,#f2f2f2)" role="img" aria-label="Photo of a pink and white furniture colour option"></div>
  <div class="abs swatch" style="left:900px;background:linear-gradient(#f0f0f0,#c8262c)" role="img" aria-label="Photo of a red furniture colour option"></div>
  <p class="abs samples-text">Nulla tempor lectus a justo vulputate ut rutrum odio porttitor. Pellentesque a consectetur lectus. Suspendisse potenti. Duis consectetur vehicula justo, imperdiet viverra leo blandit ut. Duis venenatis lorem et nibh interdum rhoncus. Sed a erat id mauris</p>
  <div class="abs view-all">View All Colours
    <svg style="position:absolute;right:6px;top:6px" width="13" height="13" viewBox="0 0 13 13"><circle cx="6.5" cy="6.5" r="6" fill="#0b6d99"/><path d="M5 3.5l3 3-3 3" fill="none" stroke="#fff" stroke-width="1.5"/></svg>
  </div>
</section>

<footer>
  <div class="abs foot"></div>
  <div class="abs fcol" style="left:188px"><h4>Customer Service</h4><ul><li>Overview</li><li>Contact Us</li><li>Delivery &amp; Returns</li><li>Privacy Policy</li><li>Terms &amp; Conditions</li></ul></div>
  <div class="abs fcol" style="left:533px"><h4>Products</h4><ul><li>News</li><li>Brands</li><li>Trade Buyers</li><li>Price Promise</li><li>The Furniture Company</li></ul></div>
  <div class="abs fcol" style="left:847px"><h4>About us</h4><ul><li>Green Policy</li><li>Testimonials &amp; Reviews</li><li>Press Office</li><li>Stores</li><li>FAQs</li></ul></div>
  <div class="abs base">
    <div class="legal">Harlow Furniture Limited - Copyright © 2011<br>Companies House No: 7402158</div>
    <div class="partner-badge" role="img" aria-label="Parent group badge"></div>
  </div>
</footer>

</body>
</html>
```